Gentle Kundalini Yoga with Gong Relaxation

I teach a gentle Kundalini Yoga class with Gong relaxation every Thursday morning from 8:30-10am at the Alder Crossing Congregational Church 17 Marbury Lane Alder Crossing. This class is unique in that I play the gong for an extended relaxation. Gongs are generally only found in established Yoga centers not in a small neighborhood yoga class. I am trying to grow this class from a current class size of 5 students. I would like to double the class size.
Updates
Project Deadline Extended
Reason: We had a blizzard on January 27 and 28 in the Boston area and I was too busy removing snow to tend to the postcard design-Thank you-Dolores Whitcombe
Industry/Entity Type
Church

```html
<!DOCTYPE html>
<html lang="en">
<head>
<meta charset="utf-8">
<title>Kundalini Yoga with Gong Relaxation – Postcard</title>
<link rel="stylesheet" href="https://fonts.googleapis.com/css2?family=Roboto+Condensed:wght@400;700&display=swap">
<style>
  :root {
    --stage: #d9d9d9;
    --card: #ffffff;
    --green: #5cb531;
    --green-dark: #3f9a22;
    --ink: #222222;
    --grey: #555555;
    --grey-light: #9a9a9a;
    --banner: rgba(60, 60, 60, 0.78);
    --photo-top: #dfe8ef;
    --photo-bottom: #b9c7a4;
  }
  * { box-sizing: border-box; margin: 0; padding: 0; }
  html, body {
    width: 1200px; height: 825px; overflow: hidden;
    background: var(--stage);
    font-family: "Roboto Condensed", "Arial Narrow", sans-serif;
  }
  .canvas { position: relative; width: 1200px; height: 825px; }
  .postcard {
    position: absolute; top: 222px;
    width: 560px; height: 380px;
    background: var(--card);
    overflow: hidden;
    box-shadow: 0 6px 18px rgba(0,0,0,0.25);
  }
  .postcard--front { left: 26px; }
  .postcard--back { left: 614px; }

  /* Front */
  .class-photo {
    position: absolute; inset: 0;
    background: linear-gradient(170deg, var(--photo-top) 0%, #e9e3dc 45%, var(--photo-bottom) 100%);
  }
  .green-band { position: absolute; inset: 0; }
  .schedule {
    position: absolute; left: 18px; top: 56px;
    color: #fff; line-height: 1.05;
  }
  .schedule__day { font-size: 22px; font-weight: 700; }
  .schedule__price { font-size: 22px; font-weight: 700; margin-top: 8px; }
  .schedule__price small { font-size: 14px; font-weight: 400; }
  .schedule__card { font-size: 16px; font-weight: 700; }
  .brand-seal {
    position: absolute; left: 410px; top: 4px;
    width: 84px; height: 84px; border-radius: 50%;
    background: #fff; border: 5px solid var(--green);
    display: flex; align-items: center; justify-content: center;
    text-align: center; color: var(--grey);
    font-size: 15px; font-weight: 700; line-height: 1;
  }
  .title-banner {
    position: absolute; left: 320px; top: 228px;
    width: 240px; padding: 8px 10px 8px 14px;
    background: var(--banner); color: #fff; line-height: 1;
  }
  .title-banner__name { font-size: 27px; font-weight: 700; }
  .title-banner__sub { font-size: 17px; margin-top: 3px; padding-left: 20px; }
  .phone {
    position: absolute; left: 336px; top: 300px;
    font-size: 30px; font-weight: 700; color: var(--grey);
  }

  /* Back */
  .back-brand {
    position: absolute; left: 40px; top: 150px; width: 240px; text-align: center;
  }
  .back-brand__seal {
    width: 70px; height: 70px; margin: 0 auto 22px;
    border-radius: 50%; border: 4px solid var(--grey-light);
    display: flex; align-items: center; justify-content: center;
    color: var(--grey); font-size: 13px; font-weight: 700; line-height: 1;
  }
  .back-brand__name { font-size: 30px; font-weight: 700; color: var(--ink); line-height: 1; }
  .back-brand__sub { font-size: 19px; color: var(--ink); }
  .venue {
    position: absolute; left: 40px; top: 318px; width: 240px;
    text-align: center; font-size: 13px; color: var(--grey); line-height: 1.3;
  }
  .divider {
    position: absolute; left: 300px; top: 40px; width: 1px; height: 310px;
    background: var(--grey-light);
  }
  .stamp-box {
    position: absolute; right: 28px; top: 26px;
    width: 66px; height: 80px; border: 1px solid var(--grey);
  }
  .address-lines { position: absolute; left: 324px; top: 160px; width: 210px; }
  .address-lines span {
    display: block; height: 44px; border-bottom: 1px dotted var(--grey);
  }
</style>
</head>
<body>
<main class="canvas">

  <section class="postcard postcard--front">
    <div class="class-photo" role="img" aria-label="Photo of a group of people seated cross-legged on mats in a bright studio, hands raised together above their heads"></div>
    <svg class="green-band" viewBox="0 0 560 380" width="560" height="380" aria-hidden="true">
      <path d="M0,0 H560 V0 H500 C320,80 170,260 0,340 Z" fill="var(--green)"/>
      <path d="M0,340 C170,260 320,80 500,0 H560" fill="none" stroke="#ffffff" stroke-width="6"/>
    </svg>
    <div class="schedule">
      <p class="schedule__day">Every Thursday Morning<br>from 8:30-10am</p>
      <p class="schedule__price">$12.00 <small>a class</small></p>
      <p class="schedule__card">10 class card for $100</p>
    </div>
    <div class="brand-seal">Alder<br>Yoga</div>
    <div class="title-banner">
      <p class="title-banner__name">Kundalini Yoga</p>
      <p class="title-banner__sub">with Gong relaxation</p>
    </div>
    <p class="phone">555-014-2730</p>
  </section>

  <section class="postcard postcard--back">
    <div class="back-brand">
      <div class="back-brand__seal">Alder<br>Yoga</div>
      <p class="back-brand__name">Kundalini Yoga</p>
      <p class="back-brand__sub">with Gong relaxation</p>
    </div>
    <p class="venue">Congregational Church 17-Marbury Lane<br>Alder Crossing</p>
    <div class="divider"></div>
    <div class="stamp-box"></div>
    <div class="address-lines"><span></span><span></span><span></span></div>
  </section>

</main>
</body>
</html>
```